New Phone Case requires logo and packaging

We need a nice and sleek logo designed along with packaging for our Premium Phone Case brand

Our Brand Name is Vaxel
Please note this has nothing to do with a Rhino so don't put a Rhino in the logo
I've also attached a file called VAXEL Logo Inspiration, which shows something along the lines of the type of text we want to use. Please note i have photoshopped that image together from another logo we had, and i liked the text, but its for you to see what direction we want to go in. Also note i have shown different variations in that image file, use your imagination with it and show us a nice and clean logo.

We would like the Brand in upper caps such as VAXEL
The brand is for Premium Phone Cases. The first thing that should come to someones mind when looking at the branding is High Quality, Premium and Modern.

The look must be high end and modern

The design must portray high quality and premium!

Also i will say "Less is More". Don't cramp many things on the packaging and logo. We just want a nice, clean cut high quality logo and packaging

I have attached images of an example packaging from a few competitors. One is a standard open from top packaging, while another is a slide out packaging. Our packaging dimensions should be the same which are Packaging dimensions
Length = 18cm
Height = 1.5cm
Depth = 9.5cm

Also note the example packaging has a transparent front section to show which case is inside, this is optional if you want to have it. If not you can cover it all up.

Font styles to use
Other font styles liked:
• Any nice font but just not the standard everyday stuff like Arial, San Serif etc as i want it to be differentiated. A Font that shows Serious Quality and one that stands out would be awesome!

Colors

Designer to choose colors to be used in the design.

Requirements
Must have
• Must be a nice and clean design
• Packaging dimensions
• Length = 18cm
• Height = 1.5cm
• Depth = 9.5cm

```html
<!DOCTYPE html>
<html lang="en">
<head>
<meta charset="UTF-8">
<title>Vaxel Packaging</title>
<link rel="stylesheet" href="https://fonts.googleapis.com/css2?family=Montserrat:wght@300;400;500&display=swap">
<style>
  :root {
    --bg: #ffffff;
    --board: #151515;
    --tray: #0b0b0d;
    --tab: #c8202a;
    --brand: #27465e;
    --ink: #f2f2f2;
    --dot-1: #3a3a3a;
    --dot-2: #555555;
    --dot-3: #7a7a7a;
    --dot-4: #a6a6a6;
    --dot-5: #dcdcdc;
    --case: #f4f4f4;
  }
  * { margin: 0; padding: 0; box-sizing: border-box; }
  html, body { width: 1200px; height: 1200px; overflow: hidden; background: var(--bg); }
  body { position: relative; font-family: "Montserrat", sans-serif; color: var(--ink); }

  .tab { position: absolute; background: var(--tab); border-radius: 14px 14px 0 0; }
  .tray { position: absolute; background: var(--tray); }
  .sleeve { position: absolute; background: var(--board); }

  /* front */
  .front-tab { left: 267px; top: 150px; width: 59px; height: 56px; }
  .front-tray { left: 117px; top: 205px; width: 361px; height: 130px; overflow: hidden; }
  .case-visual {
    position: absolute; left: 29px; top: 24px; width: 308px; height: 140px;
    border-radius: 28px; background: linear-gradient(180deg, var(--case), #dedede);
  }
  .front-sleeve { left: 111px; top: 334px; width: 372px; height: 719px; }
  .wordmark {
    position: absolute; left: 0; right: 0; text-align: center;
    font-weight: 300; color: var(--brand); letter-spacing: 0.08em;
  }
  .front-sleeve .wordmark { top: 190px; font-size: 76px; line-height: 1; }
  .dots { position: absolute; display: flex; gap: 5px; }
  .dots span { width: 10px; height: 10px; border-radius: 50%; }
  .dots span:nth-child(1) { background: var(--dot-1); }
  .dots span:nth-child(2) { background: var(--dot-2); }
  .dots span:nth-child(3) { background: var(--dot-3); }
  .dots span:nth-child(4) { background: var(--dot-4); }
  .dots span:nth-child(5) { background: var(--dot-5); }
  .front-sleeve .dots { left: 152px; top: 641px; }
  .tagline { font-size: 14px; letter-spacing: 0.12em; font-weight: 400; white-space: nowrap; }
  .front-sleeve .tagline { position: absolute; left: 0; right: 0; top: 669px; text-align: center; }

  /* side */
  .side-tab { left: 592px; top: 150px; width: 8px; height: 56px; border-radius: 4px 4px 0 0; }
  .side-tray { left: 550px; top: 205px; width: 94px; height: 130px; }
  .side-sleeve { left: 545px; top: 334px; width: 103px; height: 719px; }
  .side-sleeve .dots { left: 36px; top: 546px; flex-direction: column; }
  .side-sleeve .tagline {
    position: absolute; left: 55px; top: 685px; transform-origin: 0 0; transform: rotate(-90deg);
  }

  /* back */
  .back-tab { left: 873px; top: 150px; width: 59px; height: 56px; }
  .back-tray { left: 722px; top: 205px; width: 361px; height: 130px; }
  .back-sleeve { left: 716px; top: 334px; width: 373px; height: 719px; }
  .back-sleeve .wordmark { top: 44px; font-size: 44px; line-height: 1; }
  .intro { position: absolute; left: 65px; width: 240px; top: 158px; font-size: 7.5px; line-height: 1.35; }
  .intro p + p { margin-top: 22px; }
  .rule { position: absolute; left: 66px; top: 278px; width: 239px; height: 2px; background: var(--ink); }
  .languages { position: absolute; left: 20px; right: 18px; top: 305px; }
  .language { display: flex; align-items: center; gap: 14px; margin-bottom: 14px; }
  .language-mark { flex: 0 0 12px; height: 12px; border-radius: 50%; background: #9a9a9a; }
  .language p { font-size: 7px; line-height: 1.33; text-align: justify; }
  .certifications { position: absolute; left: 110px; top: 671px; display: flex; gap: 8px; align-items: center; }
  .cert { background: var(--ink); }
  .cert-square { width: 22px; height: 20px; border-radius: 3px; }
  .cert-circle { width: 18px; height: 18px; border-radius: 50%; }
  .cert-wide { width: 44px; height: 16px; border-radius: 3px; }
</style>
</head>
<body>
  <!-- front panel -->
  <div class="tab front-tab"></div>
  <div class="tray front-tray">
    <div class="case-visual" role="img" aria-label="White phone case with camera cut-out inside the tray"></div>
  </div>
  <section class="sleeve front-sleeve">
    <div class="wordmark">VAXEL</div>
    <div class="dots"><span></span><span></span><span></span><span></span><span></span></div>
    <div class="tagline">PREMIUM PHONE CASES</div>
  </section>

  <!-- side panel -->
  <div class="tab side-tab"></div>
  <div class="tray side-tray"></div>
  <section class="sleeve side-sleeve">
    <div class="dots"><span></span><span></span><span></span><span></span><span></span></div>
    <div class="tagline">PREMIUM PHONE CASES</div>
  </section>

  <!-- back panel -->
  <div class="tab back-tab"></div>
  <div class="tray back-tray"></div>
  <section class="sleeve back-sleeve">
    <div class="wordmark">VAXEL</div>
    <div class="intro">
      <p>Vaxel cases are shaped to fit your phone precisely and protect it every day.</p>
      <p>Each case is made from durable materials with a soft touch finish and raised edges.</p>
      <p>Designed to keep your phone slim, light and safe.</p>
    </div>
    <div class="rule"></div>
    <div class="languages">
      <div class="language"><span class="language-mark"></span>
        <p>Thank you for choosing Vaxel. Slide the case onto your phone starting at the top corner, then press along the edges until it sits firmly. Clean with a soft dry cloth. Keep away from heat and sharp objects. Keep this packaging for future reference.</p></div>
      <div class="language"><span class="language-mark"></span>
        <p>Merci d'avoir choisi Vaxel. Glissez la coque sur votre téléphone en commençant par le coin supérieur, puis appuyez le long des bords. Nettoyez avec un chiffon doux et sec. Tenez à l'écart de la chaleur et des objets pointus.</p></div>
      <div class="language"><span class="language-mark"></span>
        <p>Danke, dass Sie Vaxel gewählt haben. Schieben Sie die Hülle von der oberen Ecke aus auf Ihr Telefon und drücken Sie die Ränder fest. Mit einem weichen, trockenen Tuch reinigen. Von Hitze und spitzen Gegenständen fernhalten.</p></div>
      <div class="language"><span class="language-mark"></span>
        <p>Grazie per aver scelto Vaxel. Inserisci la cover sul telefono partendo dall'angolo superiore, poi premi lungo i bordi. Pulisci con un panno morbido e asciutto. Tieni lontano da fonti di calore e oggetti appuntiti.</p></div>
    </div>
    <div class="certifications">
      <span class="cert cert-square"></span>
      <span class="cert cert-circle"></span>
      <span class="cert cert-wide"></span>
      <span class="cert cert-circle"></span>
      <span class="cert cert-square"></span>
    </div>
  </section>
</body>
</html>
```